Multi App design - layout and graphic suggestions to our new app

Update:
Making a modern and futuristic design of a multifunctional app.
Attached is a description of some of the functionalities.
We need this innovative elegant design on buttons, menu, screens and other elements to be applied onto several mobile screens to choose a style that can be chosen.
Future apps will even include robot assistance, new navigation logic and 3Dish style and several templates to variate the style (look and feel).
Looking forward to see some really new style of futuristic apps!
(We like the app vupa.com - although our design shall be even more modern and creative)

Multi-function app

We would like to have a design suggestion for a multi-function app.

The design shall show front end design as well as navigation and UI/UX user interface

It’s and generic shopping app enabling a long list of services where end user get a menu which is graphical and can be extended with new services as well as customized by end user.
Each service contains functionality as well as content and findings.
Among 5-10 initial services are:

• Shopping assistant and Travel assistant – finding relevant shops/museum and products nearby – sorted by Geofence and Beacons for presenting information - or find stores and experiences
• Loyalty points / Contests and bonus points - preferences and sharing reviews 
• QR and Barcode reader – for increased information
• Campaigns
• Support and feedback

Flexible application - with simple possibility to add new services and allow the user to control the order of the menu / own top menu
Simpler social sharing - reviews, feedback, loyalty points across shops etc.
Easy user management - turn off shops or functionality - without uninstalling

Target Market(s)

End user

Industry/Entity Type

Inn

Requirements
Must have
• The design shall show front end design as well as navigation and UI/UX user interface.
• Attached is your logo and colors with codes

```html
<!DOCTYPE html>
<html lang="en">
<head>
<meta charset="utf-8">
<title>Places</title>
<link href="https://fonts.googleapis.com/css2?family=Lato:wght@300;400;700&display=swap" rel="stylesheet">
<style>
:root{
  --teal:#0e9297;
  --teal-text:#11979b;
  --screen-bg:#f1f1f1;
  --card-bg:#ffffff;
  --title:#2f3438;
  --muted:#7d8286;
  --tab-bg:rgba(255,255,255,0.96);
  --icon-dark:#161616;
}
*{box-sizing:border-box;margin:0;padding:0}
html,body{width:675px;height:1200px;overflow:hidden;background:var(--screen-bg)}
body{font-family:'Lato',sans-serif;position:relative}
.status-bar{position:absolute;top:0;left:0;width:675px;height:40px;color:#fff;font-size:20px;display:flex;align-items:center;padding:0 10px;z-index:3}
.status-bar .signal{display:flex;gap:3px;margin-right:6px}
.status-bar .signal span{width:9px;height:9px;border-radius:50%;background:#fff}
.status-bar .time{position:absolute;left:0;right:0;text-align:center;pointer-events:none}
.status-bar .battery{margin-left:auto;display:flex;align-items:center;gap:6px}
.app-header{position:absolute;top:0;left:0;width:675px;height:115px;background:var(--teal)}
.app-header .title{position:absolute;top:58px;left:0;width:100%;text-align:center;color:#fff;font-weight:700;font-size:28px;letter-spacing:0.5px}
.app-header .home{position:absolute;left:36px;top:57px}
.app-header .search{position:absolute;left:605px;top:57px}
.content{position:absolute;top:115px;left:0;width:675px;height:997px;overflow:hidden}
.nearby{position:absolute;left:36px;top:36px;width:603px;height:71px;background:var(--card-bg);border-radius:3px;display:flex;align-items:center;padding-left:17px}
.nearby svg{margin-right:19px}
.nearby span{color:var(--teal-text);font-weight:700;font-size:24px}
.place-card{position:absolute;width:288px;height:287px;background:var(--card-bg);border-radius:3px;overflow:hidden}
.place-card .photo{height:180px}
.place-card h2{font-weight:400;font-size:24px;color:var(--title);margin:24px 0 0 19px}
.place-card p{font-weight:300;font-size:20px;color:var(--muted);margin:12px 0 0 19px}
.col-a{left:36px}.col-b{left:351px}
.row-1{top:144px}.row-2{top:468px}.row-3{top:792px}
.photo-coffee{background:linear-gradient(160deg,#1f3552 0%,#324a63 45%,#6d5a45 75%,#2a2623 100%)}
.photo-friends{background:linear-gradient(150deg,#5a2f22 0%,#9c5b3e 40%,#d3b39a 70%,#7a4a34 100%)}
.photo-harbour{background:linear-gradient(180deg,#3f6b2a 0%,#c9cfc8 40%,#8a4e3a 55%,#2f5a2c 100%)}
.photo-night{background:linear-gradient(170deg,#2a4fb8 0%,#6a3f9c 45%,#2c2440 80%,#1b1a2a 100%)}
.photo-gallery{background:linear-gradient(160deg,#4a4f5a 0%,#6b7078 50%,#8a7a66 80%,#5c5a58 100%)}
.photo-dining{background:linear-gradient(170deg,#6b4a36 0%,#a7876d 45%,#d9cfc4 75%,#7d5a44 100%)}
.tab-bar{position:absolute;left:0;top:1112px;width:675px;height:88px;background:var(--tab-bg);display:flex;box-shadow:0 -1px 6px rgba(0,0,0,0.05)}
.tab{flex:1;display:flex;flex-direction:column;align-items:center;padding-top:15px;font-size:21px;color:#555}
.tab svg{height:34px;margin-bottom:8px}
</style>
</head>
<body>
<div class="status-bar">
  <div class="signal"><span></span><span></span><span></span><span></span><span></span></div>
  <span>Vela</span>
  <svg width="24" height="18" viewBox="0 0 24 18" style="margin-left:6px"><path d="M12 16l-3-3.5a4.5 4.5 0 0 1 6 0zM5 9a10 10 0 0 1 14 0l-2 2a7 7 0 0 0-10 0zM1 5a15 15 0 0 1 22 0l-2 2A12 12 0 0 0 3 7z" fill="#fff"/></svg>
  <span class="time">9:41 AM</span>
  <div class="battery"><span>100%</span>
    <svg width="42" height="18" viewBox="0 0 42 18"><rect x="1" y="1" width="36" height="16" rx="3" fill="none" stroke="#fff" stroke-width="1.5"/><rect x="3" y="3" width="32" height="12" rx="1.5" fill="#fff"/><rect x="38.5" y="6" width="2.5" height="6" rx="1" fill="#fff"/></svg>
  </div>
</div>

<header class="app-header">
  <svg class="home" width="32" height="32" viewBox="0 0 32 32" fill="none" stroke="#fff" stroke-width="1.8"><path d="M3 15L16 3l13 12M6 12v17h7v-9h6v9h7V12"/></svg>
  <h1 class="title">PLACES</h1>
  <svg class="search" width="34" height="34" viewBox="0 0 34 34" fill="none" stroke="#fff" stroke-width="2"><circle cx="14" cy="14" r="11"/><path d="M22 22l10 10"/></svg>
</header>

<main class="content">
  <div class="nearby">
  <svg width="26" height="36" viewBox="0 0 26 36" fill="none" stroke="var(--teal-text)" stroke-width="1.8"><path d="M13 34S2 20 2 12.5a11 11 0 0 1 22 0C24 20 13 34 13 34z"/><circle cx="13" cy="12.5" r="4"/></svg>
  <span>Browse good place nearby</span>
  </div>

  <article class="place-card col-a row-1"><div class="photo photo-coffee" role="img" aria-label="Coffee bar interior with counter and hanging lamps"></div><h2>Best for coffee</h2><p>By Mira Solen</p></article>
  <article class="place-card col-b row-1"><div class="photo photo-friends" role="img" aria-label="Friends relaxing together at a busy bar"></div><h2>Hangout with friends</h2><p>By Lina Corvo</p></article>
  <article class="place-card col-a row-2"><div class="photo photo-harbour" role="img" aria-label="Harbour with wooden houses reflected in the water"></div><h2>Awesome sightseeing</h2><p>By Peter Halvik</p></article>
  <article class="place-card col-b row-2"><div class="photo photo-night" role="img" aria-label="Crowd at an outdoor evening venue under blue light"></div><h2>Enjoying night</h2><p>By Anton Brel</p></article>
  <article class="place-card col-a row-3"><div class="photo photo-gallery" role="img" aria-label="Visitors walking past paintings in a gallery"></div></article>
  <article class="place-card col-b row-3"><div class="photo photo-dining" role="img" aria-label="Elegant dining hall with set tables and chandeliers"></div></article>
</main>

<nav class="tab-bar">
  <div class="tab"><svg width="38" viewBox="0 0 38 34" fill="none" stroke="var(--teal)" stroke-width="2.2" stroke-linejoin="round"><path d="M2 5l11-3 12 3 11-3v27l-11 3-12-3-11 3z"/><path d="M13 2v27M25 5v27"/></svg><span>Places</span></div>
  <div class="tab"><svg width="34" viewBox="0 0 34 34" fill="none" stroke="var(--icon-dark)" stroke-width="3.2"><path d="M2 11V2h9M23 2h9v9M32 23v9h-9M11 32H2v-9"/></svg><span>Scan</span></div>
  <div class="tab"><svg width="30" viewBox="0 0 30 40" fill="var(--icon-dark)"><path d="M8 22l-6 14 6-2 3 5 4-12zM22 22l6 14-6-2-3 5-4-12z"/><circle cx="15" cy="14" r="13"/><circle cx="15" cy="14" r="8" fill="none" stroke="#fff" stroke-width="2"/></svg><span>Point</span></div>
  <div class="tab"><svg width="34" viewBox="0 0 34 34" fill="var(--icon-dark)"><circle cx="17" cy="9" r="8"/><path d="M1 34c0-10 7-15 16-15s16 5 16 15z"/></svg><span>Profile</span></div>
</nav>
</body>
</html>
```